Environmental Plastics Infographic

We need a series of infographics that can be used individually or as a combined presentation. We'd like the combined piece to include an introduction and conclusion along with 4-5 infographics. Each infographic (information unit) should also work as a standalone. We are trying to help people visualize size proportions and ratios to put carbon footprint/life cycle data for EPS foam packaging in perspective. We are looking for something creative to help people understand what the figures represent in terms they are familiar with.
To view our typical company design/style please see our website at www.trellamark.org. Our primary RGB colors are: (187,140,9); (94,47,29); (94,138,164); and (164,167,15). Secondary RGB colors are (249,162,28) and (218,210,208). Our title/header font is DIN Next LT Pro and our copy font is Calibri 10.5 pt. We can deviate from the font specification if beneficial and welcome interesting text treatments and typography.
We want sufficient white space with easy to grasp message concept with visual components. The attachment showing data points present concepts on how to show the data impacts but are only representative of a baseline concept - we are confident a professional designer can do a much better job with better visual presentation.
Target Market(s)
The audience is international brand manufacturers (brightmoor, kavo), US legislators & government agencies.
Nice to have
- Other creative ideas on how to present this messaging is encouraged.

```html
<!DOCTYPE html>
<html lang="en">
<head>
<meta charset="utf-8">
<title>EPS Life Cycle</title>
<link rel="stylesheet" href="https://fonts.googleapis.com/css2?family=Montserrat:wght@500;600;700;800;900&family=Open+Sans:ital,wght@0,400;1,400;1,600&display=swap">
<style>
:root{
  --brown:#5e2f1d;
  --gold:#b8902f;
  --gold-bar:#b8922e;
  --olive:#a0a63a;
  --olive-bar:#a3a83b;
  --olive-title:#9ea53a;
  --white:#ffffff;
  --sky:#6ccdf2;
  --leaf:#9fd08a;
  --box:#e9e9ea;
  --shadow:#8a8f2e;
}
*{margin:0;padding:0;box-sizing:border-box}
html,body{width:1200px;height:3797px;overflow:hidden;background:var(--white)}
body{position:relative;font-family:"Montserrat",sans-serif;color:var(--brown)}
.abs{position:absolute}
.top-bar{left:0;top:0;width:1200px;height:42px;background:var(--brown)}
.title{left:70px;top:100px;font-weight:900;font-size:92px;line-height:94px;color:var(--olive-title);letter-spacing:1px}
.title-tag{left:72px;top:313px;width:570px;height:72px;background:var(--brown);color:var(--white);font-weight:700;font-size:48px;letter-spacing:5px;line-height:72px;padding-left:14px}
.intro{left:72px;top:408px;font-family:"Open Sans",sans-serif;font-style:italic;font-size:26px;line-height:31px;color:#222}
.globe{left:790px;top:114px;width:340px;height:370px;border-radius:50%;background:radial-gradient(circle at 55% 50%,var(--sky) 0 55%,var(--leaf) 56% 70%,transparent 71%)}
.car{left:80px;top:664px;width:254px;height:80px;background:var(--brown);border-radius:40px 60px 14px 14px}
.gears{left:930px;top:649px;width:148px;height:126px;background:var(--brown);border-radius:50%}
.bar{bottom:calc(3797px - 1215px)}
.bubble{border-radius:50%;display:flex;flex-direction:column;align-items:center;justify-content:center;font-weight:600;transform:translateX(-50%)}
.bubble b{font-size:40px;line-height:40px;font-weight:600}
.bubble small{font-size:22px;font-weight:500}
.b-light{background:var(--white);border:7px solid var(--gold);color:var(--brown)}
.b-dark{background:var(--olive-bar);border:8px solid var(--brown);color:var(--white)}
.pill{transform:translateX(-50%);width:112px;height:42px;border-radius:21px;background:var(--brown);color:var(--white);font-weight:500;font-size:26px;line-height:42px;text-align:center}
.axis{height:5px;background:var(--brown)}
.axis-label{font-weight:500;font-size:31px;transform:translateX(-50%);top:1228px;white-space:nowrap}
.axis-band{height:45px;background:var(--brown);color:var(--white);font-weight:500;font-size:27px;line-height:45px;text-align:center}
.section-energy{left:0;top:1437px;width:1200px;height:784px;background:var(--gold)}
.section-water{left:0;top:2244px;width:1200px;height:1350px;background:var(--olive)}
.heading{color:var(--white);font-weight:900;font-size:74px;line-height:78px;letter-spacing:1px}
.note{color:var(--white);font-family:"Open Sans",sans-serif;font-style:italic;font-size:25px;line-height:32px}
.trees{left:816px;width:323px;height:355px;background:linear-gradient(180deg,#f3f0e6 0 30%,var(--leaf) 30%)}
.bulb{left:72px;width:127px;height:190px;background:var(--white);border-radius:64px 64px 20px 20px}
.stat{color:var(--white);font-weight:800;font-size:56px;line-height:54px}
.eps-badge{left:583px;width:209px;height:209px;border-radius:50%;background:var(--white);color:var(--gold);font-weight:900;font-size:74px;line-height:209px;text-align:center}
.drop{left:1044px}
.label-it{color:var(--white);font-family:"Open Sans",sans-serif;font-style:italic;font-size:26px;line-height:32px;text-align:center;transform:translateX(-50%);white-space:nowrap}
.pool{left:114px;width:332px;height:199px;background:var(--sky);border-radius:50%}
.product{background:linear-gradient(180deg,var(--box) 0 75%,var(--shadow) 75%);border-radius:10px}
.kraft{background:linear-gradient(180deg,#a87a55 0 75%,var(--shadow) 75%);border-radius:10px}
.equals{left:541px;width:57px;height:60px}
.equals i{display:block;height:16px;background:var(--white);margin-bottom:24px}
.big-cap{color:var(--white);font-weight:700;font-size:34px;line-height:40px;letter-spacing:3px;text-align:center;transform:translateX(-50%);white-space:nowrap}
.small-cap{color:var(--white);font-weight:600;font-size:30px;line-height:37px;text-align:center;transform:translateX(-50%);white-space:nowrap}
.footer-mark{left:120px;top:3637px;width:133px;height:133px;border-radius:50%;background:var(--gold)}
.footer-name{left:266px;top:3678px;font-weight:500;font-size:23px;line-height:24px;color:var(--brown)}
.footer-url{left:528px;top:3680px;font-weight:700;font-size:33px;letter-spacing:7px;color:var(--brown);white-space:nowrap}
</style>
</head>
<body>
<div class="abs top-bar"></div>

<header>
  <h1 class="abs title">EPS<br>LIFE CYCLE</h1>
  <div class="abs title-tag">GLOBAL WARMING</div>
  <p class="abs intro">EPS has a very low global warming impact<br>compared to other packaging materials.</p>
  <div class="abs globe" role="img" aria-label="Illustration of the Earth wrapped by leafy vines"></div>
</header>

<section class="chart" aria-label="CO2 emissions comparison">
  <div class="abs car" role="img" aria-label="Car illustration"></div>
  <div class="abs gears" role="img" aria-label="Gears illustration"></div>

  <div class="abs bubble b-light" style="left:180px;top:983px;width:114px;height:114px"><b style="font-size:30px;line-height:30px">115.5</b><small>kg</small></div>
  <div class="abs pill" style="left:180px;top:1110px">CO2</div>
  <div class="abs bar" style="left:148px;width:65px;height:51px;background:var(--gold-bar)"></div>

  <div class="abs bubble b-dark" style="left:357px;top:889px;width:133px;height:133px"><b>5360</b><small>kg</small></div>
  <div class="abs pill" style="left:357px;top:1025px">CO2</div>
  <div class="abs bar" style="left:323px;width:65px;height:137px;background:var(--olive-bar)"></div>

  <div class="abs bubble b-light" style="left:526px;top:801px;width:152px;height:152px"><b>5775</b><small>kg</small></div>
  <div class="abs pill" style="left:526px;top:969px">CO2</div>
  <div class="abs bar" style="left:494px;width:64px;height:194px;background:var(--gold-bar)"></div>

  <div class="abs bubble b-light" style="left:703px;top:567px;width:165px;height:165px"><b style="font-size:44px">11550</b><small>kg</small></div>
  <div class="abs pill" style="left:703px;top:745px">CO2</div>
  <div class="abs bar" style="left:674px;width:63px;height:418px;background:var(--gold-bar)"></div>

  <div class="abs bubble b-dark" style="left:1003px;top:887px;width:133px;height:133px"><b>5360</b><small>kg</small></div>
  <div class="abs pill" style="left:1003px;top:1025px">CO2</div>
  <div class="abs bar" style="left:970px;width:65px;height:137px;background:var(--olive-bar)"></div>

  <div class="abs axis" style="left:91px;top:1213px;width:682px"></div>
  <div class="abs axis" style="left:896px;top:1213px;width:219px"></div>
  <span class="abs axis-label" style="left:180px">1 km</span>
  <span class="abs axis-label" style="left:357px">31 km</span>
  <span class="abs axis-label" style="left:526px">50 km</span>
  <span class="abs axis-label" style="left:691px">100 km</span>
  <span class="abs axis-label" style="left:1006px">1 TON EPS</span>
  <div class="abs axis-band" style="left:95px;top:1278px;width:676px">Driving Distance</div>
  <div class="abs axis-band" style="left:896px;top:1278px;width:219px">Manufacturing</div>
</section>

<section class="abs section-energy">
  <h2 class="abs heading" style="left:72px;top:91px">LIFE CYCLE<br>NON-RENEWABLE<br>ENERGY USE</h2>
  <p class="abs note" style="left:72px;top:326px;font-size:24px;line-height:31px">EPS energy consumption for the manufacture<br>of 1 ton of packaging material is equivalent to<br>300 hours of light for a single lightbulb.</p>
  <div class="abs trees" style="top:68px" role="img" aria-label="Illustration of sun, cloud and two trees"></div>
  <div class="abs bulb" style="top:518px" role="img" aria-label="Lightbulb icon with number one"></div>
  <p class="abs stat" style="left:228px;top:558px">100 Watt<br>360 MJ</p>
  <div class="abs eps-badge" style="top:509px">EPS</div>
  <p class="abs stat" style="left:822px;top:570px">1 Ton<br>108,000 MJ</p>
</section>

<section class="abs section-water">
  <h2 class="abs heading" style="left:72px;top:101px">LIFE CYCLE<br>WATER CONSUMPTION</h2>
  <p class="abs note" style="left:68px;top:256px">The amount of water used to manufacture 1,000 EPS shipping contaiers<br>is the equivalent of xx swimming pools.</p>
  <svg class="abs drop" style="top:101px" width="86" height="113" viewBox="0 0 86 113" aria-hidden="true"><path d="M43 4 C60 34 82 56 82 76 A39 33 0 0 1 4 76 C4 56 26 34 43 4Z" fill="var(--sky)" stroke="var(--brown)" stroke-width="6"/></svg>

  <p class="abs label-it" style="left:277px;top:374px">One 40x20 Ft Swimming Pool<br>(Avg 4 Ft Depth)</p>
  <p class="abs label-it" style="left:887px;top:374px">A typical EPS shipping container<br>15x13x12 inches weighs 2 lbs</p>
  <div class="abs pool" style="top:481px" role="img" aria-label="Swimming pool illustration"></div>
  <div class="abs equals" style="top:546px" aria-label="equals"><i></i><i></i></div>
  <div class="abs product" style="left:674px;top:452px;width:427px;height:237px" role="img" aria-label="White EPS shipping container illustration"></div>
  <p class="abs big-cap" style="left:280px;top:708px">24,000<br>GALLONS</p>
  <p class="abs big-cap" style="left:889px;top:708px">1,000 EPS<br>CONTAINERS</p>

  <p class="abs note" style="left:85px;top:855px">The amount of water used to manufacture 1,000 EPS shipping containers<br>is a miniscule amount compared to corrugated paper.</p>
  <div class="abs product" style="left:66px;top:955px;width:428px;height:209px" role="img" aria-label="White EPS container illustration"></div>
  <div class="abs kraft" style="left:674px;top:955px;width:427px;height:209px" role="img" aria-label="Open corrugated cardboard box illustration"></div>
  <p class="abs small-cap" style="left:280px;top:1183px">1 Ton<br>uses xxx gallons<br>of water</p>
  <p class="abs small-cap" style="left:908px;top:1183px">1 Ton<br>uses xxx gallons<br>of water</p>
</section>

<footer>
  <div class="abs footer-mark"></div>
  <span class="abs footer-name">Trellamark<br>Alliance</span>
  <span class="abs footer-url">WWW.TRELLAMARK.ORG</span>
</footer>
</body>
</html>
```